LVT, Inc. business card design

LVT, Inc is a distributor of fragrances and cosmetics globally tht sells to retailers, wholesalers and coporations

The card design should be elegant and serious .

They recently open a state of the art facility that I would like to tie in the card design to . See pictures or go to rk7buildworks.example and view the Scent Hub of Norland building and reception area for design ideas . the Building roof is all solar panel as well .

Brimlow Market(s)

Corporations and stores like Brimlow, Fen Dale

Industry/Entity Type

Business

Contact Information for Business Card

On the front
LVT, Inc.
Brand name distributors of fragrances and beauty products
On the back :

Tomas Vrell
President
Phone (icon) 555.210.4800 ext. 101 &102
Cell ( icon) 555.947.2063
email ( icon) tomas@scent-hub.example
fax ( icon) 555.210.4813
website: www.scent-hub.example

4417 Birchlow Road
Ronkonkoma, NY 11999

Font styles to use
Script

Colors
33a6d7
0492cd
ffffff
0655a3

Requirements
Must have
• Sharp design easily read and some design feature or accent of color to make it look like a beauty company very high end but also corporate.
• Need more creativity!!
• LVT,Inc. in a creative fashion
Nice to have
• Blue shades
• Would like to see some brush stroke designs for LVT incorporating silver foil
Should not have
• Faces, facial elements, perfume bottles, flowers ,
• Not to read Scent Hub of Norland

```html
<!DOCTYPE html>
<html lang="en">
<head>
<meta charset="utf-8">
<title>LVT, Inc. — Business Card Proposal</title>
<link href="https://fonts.googleapis.com/css2?family=Jost:wght@300;400&family=Bebas+Neue&display=swap" rel="stylesheet">
<style>
  :root {
    --page-bg: #ffffff;
    --title-grey: #c4c4c4;
    --rule-grey: #dcdcdc;
    --card-blue-light: #0a84b3;
    --card-blue: #0a6e9f;
    --card-blue-deep: #064c84;
    --band-white: #f4f6f7;
    --ink-blue: #0a6a99;
    --white: #ffffff;
  }
  * { box-sizing: border-box; margin: 0; padding: 0; }
  html, body { width: 1200px; height: 1200px; overflow: hidden; background: var(--page-bg); }
  .sheet { position: relative; width: 1200px; height: 1200px; font-family: "Jost", sans-serif; }

  .sheet-title {
    position: absolute; left: 64px; top: 112px;
    font-family: "Bebas Neue", sans-serif; font-weight: 400; font-size: 48px; letter-spacing: 0.5px;
    color: var(--title-grey); line-height: 1;
  }
  .sheet-rule { position: absolute; left: 48px; right: 48px; top: 167px; height: 1px; background: var(--rule-grey); }

  .card {
    position: absolute; left: 285px; width: 630px; height: 360px; overflow: hidden;
    background: radial-gradient(ellipse at 40% 35%, var(--card-blue-light) 0%, var(--card-blue) 45%, var(--card-blue-deep) 100%);
    box-shadow: 0 6px 18px rgba(0,0,0,0.18);
    color: var(--white);
  }
  .card--front { top: 250px; }
  .card--back { top: 660px; }

  /* Front */
  .front-mark {
    position: absolute; left: 26px; top: 48px;
    font-weight: 300; font-size: 128px; line-height: 1; letter-spacing: 2px;
  }
  .front-band {
    position: absolute; left: 0; right: 0; top: 168px; height: 74px; background: var(--band-white);
    display: flex; align-items: center; padding-left: 28px;
  }
  .front-tagline { font-size: 19px; font-weight: 400; color: var(--ink-blue); }

  /* Back */
  .back-band { position: absolute; left: 0; right: 0; top: 22px; height: 160px; background: var(--band-white); }
  .back-panel {
    position: absolute; left: 0; top: 152px; width: 46%; height: 30px;
    background: var(--card-blue);
  }
  .back-name {
    position: absolute; left: 22px; top: 62px;
    font-weight: 300; font-size: 92px; line-height: 1; color: var(--ink-blue); white-space: nowrap;
  }
  .back-role { position: absolute; left: 26px; top: 196px; font-size: 30px; font-weight: 300; line-height: 1.1; }
  .back-company { position: absolute; left: 26px; top: 236px; font-size: 15px; font-weight: 300; }

  .contact-list {
    position: absolute; left: 322px; top: 206px; list-style: none;
    font-size: 16px; font-weight: 300; line-height: 26px;
  }
  .contact-list li { display: flex; align-items: center; gap: 10px; white-space: nowrap; }
  .contact-icon { width: 15px; height: 15px; flex: none; }
</style>
</head>
<body>
<div class="sheet">
  <h1 class="sheet-title">BIZC PROPOSAL</h1>
  <div class="sheet-rule"></div>

  <section class="card card--front" aria-label="Card front">
    <div class="front-mark">LVT</div>
    <div class="front-band">
      <p class="front-tagline">Brand name distributors of fragrances and beauty products</p>
    </div>
  </section>

  <section class="card card--back" aria-label="Card back">
    <div class="back-band"></div>
    <div class="back-panel"></div>
    <div class="back-name">Tomas Vrell</div>
    <div class="back-role">President</div>
    <div class="back-company">LVT, Inc.</div>

    <ul class="contact-list">
      <li>
        <svg class="contact-icon" viewBox="0 0 16 16" aria-hidden="true"><rect x="0" y="0" width="16" height="16" rx="3" fill="#fff"/><path d="M5 3.5c-.8.4-1.5 1.3-1 2.8 1 2.8 3 4.9 5.8 5.9 1.4.5 2.4-.2 2.8-1l-1.8-1.6-1.2.8c-1.3-.6-2.4-1.7-3-3l.8-1.2z" fill="#0a6e9f"/></svg>
        555.210.4800 ext. 101 &amp; 102
      </li>
      <li>
        <svg class="contact-icon" viewBox="0 0 16 16" aria-hidden="true"><rect x="4" y="1" width="8" height="14" rx="1.5" fill="none" stroke="#fff" stroke-width="1.6"/><circle cx="8" cy="12.3" r="0.9" fill="#fff"/></svg>
        555.947.2063
      </li>
      <li>
        <svg class="contact-icon" viewBox="0 0 16 16" aria-hidden="true"><rect x="1" y="3" width="14" height="10" fill="#fff"/><path d="M1 3l7 5.5L15 3" fill="none" stroke="#0a6e9f" stroke-width="1.3"/></svg>
        tomas@scent-hub.example
      </li>
      <li>
        <svg class="contact-icon" viewBox="0 0 16 16" aria-hidden="true"><rect x="1" y="5" width="14" height="10" rx="1" fill="#fff"/><rect x="4" y="1" width="8" height="5" fill="#fff"/><rect x="4" y="8" width="8" height="1.3" fill="#0a6e9f"/><rect x="4" y="10.8" width="8" height="1.3" fill="#0a6e9f"/></svg>
        555.210.4813
      </li>
      <li>
        <svg class="contact-icon" viewBox="0 0 16 16" aria-hidden="true"><circle cx="8" cy="8" r="7" fill="#fff"/><ellipse cx="8" cy="8" rx="3" ry="7" fill="none" stroke="#0a6e9f" stroke-width="1"/><path d="M1 8h14" stroke="#0a6e9f" stroke-width="1"/></svg>
        www.scent-hub.example
      </li>
    </ul>
  </section>
</div>
</body>
</html>
```